High end Sports Bar/ Restaurant Postcard Design

We are a high end sports bar/restaurant in forest hills on Benning street, we have high quality bar food, 24 draft beers, wine on tap and a great selection of whiskeys & scotches.
What we need is a brightly colored postcard that advertises our weekly events. It must be easy to read but eye-catching and full of fun images that will want to make people come in and drink & eat!
We are called Harlow Commons and have a gastropub feel with one entire wall covered in brick but with 9 t.v's all with audio for all sports games. We are definitely a restaurant too so its not all about sports however we will be carrying the GBX & Coastal Victory League Soccer packages.
On the back of the card we would like to advertise our lunch menu is Monday to Friday 10a.m - 3p.m. Dinner is Sunday - Monday 3p.m - 11p.m and Brunch on Saturday & Sunday. Late night bar menu also available Thursday, Friday & Saturday from 11p.m - 1a.m
Address: 54-16 Benning Street, Forest Hills, N.Y 11382 Phone number: 718 555.0143

Reason: We are extending the deadline to give us time to figure out which design is best for us, thank you all for your participation

Target Market(s)

21 - 45 year olds

Industry/Entity Type

Restaurant

Requirements
Must have
• Each individual days event must be eye-catching yet easy to read.

```html
<!DOCTYPE html>
<html lang="en">
<head>
<meta charset="utf-8">
<title>Harlow Commons – Hours Postcard</title>
<link rel="stylesheet" href="https://fonts.googleapis.com/css2?family=Graduate&family=Norican&family=Yanone+Kaffeesatz:wght@400;600&family=Zilla+Slab:wght@500&display=swap">
<style>
  :root{
    --paper:#ffffff;
    --frame:#b9b9b9;
    --ink:#000000;
    --red:#d0222a;
    --lunch:#13b5c2;
    --dinner:#1b8fd0;
    --brunch:#ef9a22;
    --late:#6154a4;
    --white:#ffffff;
  }
  html,body{margin:0;padding:0;overflow:hidden;background:var(--paper);}
  .card{
    position:relative;width:1200px;height:930px;overflow:hidden;
    background:var(--paper);box-sizing:border-box;border:1px solid var(--frame);
  }
  .bar{position:absolute;}
  .bar--top{left:112px;top:29px;width:789px;height:50px;background:var(--red);}
  .bar--corner{left:29px;top:29px;width:26px;height:50px;background:var(--red);}
  .bar--side{left:29px;top:155px;width:26px;height:744px;background:var(--red);}
  .band{left:64px;top:90px;width:837px;height:53px;background:var(--ink);}
  .column{left:64px;top:29px;width:33px;height:871px;background:var(--ink);}

  .name-letter{
    position:absolute;font-family:"Zilla Slab",serif;font-weight:500;
    color:var(--white);font-size:46px;line-height:1;text-align:center;
  }
  .name-letter--out{color:var(--ink);}
  .name-row{
    position:absolute;left:100px;top:93px;margin:0;
    font-family:"Zilla Slab",serif;font-weight:500;font-size:46px;line-height:1;
    color:var(--white);letter-spacing:3px;
  }
  .name-column{
    position:absolute;left:64px;top:149px;width:33px;margin:0;
    font-family:"Zilla Slab",serif;font-weight:500;font-size:40px;line-height:44px;
    color:var(--white);text-align:center;
  }
  .name-column span{display:block;}

  .address{
    position:absolute;right:313px;top:101px;margin:0;
    font-family:"Yanone Kaffeesatz",sans-serif;font-weight:600;font-size:30px;
    line-height:1;color:var(--red);white-space:nowrap;
  }
  .address__label{
    font-family:"Graduate",serif;font-size:13px;color:var(--white);
    letter-spacing:1px;margin-right:6px;vertical-align:middle;
  }
  .phone{
    position:absolute;left:80px;top:880px;margin:0;transform-origin:0 0;
    transform:rotate(-90deg) translateY(-50%);white-space:nowrap;
    font-family:"Yanone Kaffeesatz",sans-serif;font-weight:600;font-size:30px;
    line-height:1;color:var(--red);letter-spacing:1px;
  }
  .phone__label{
    font-family:"Graduate",serif;font-size:13px;color:var(--white);
    margin-right:6px;vertical-align:middle;
  }

  .hours{
    position:absolute;left:112px;width:467px;box-sizing:border-box;
    padding:10px 18px;color:var(--white);
  }
  .hours--lunch{top:154px;height:118px;background:var(--lunch);}
  .hours--dinner{top:289px;height:119px;background:var(--dinner);}
  .hours--brunch{top:423px;height:118px;background:var(--brunch);}
  .hours--late{top:553px;height:345px;background:var(--late);}
  .hours__title{
    margin:0;font-family:"Graduate",serif;font-weight:400;font-size:36px;
    line-height:44px;color:var(--ink);letter-spacing:2px;white-space:nowrap;
  }
  .hours__served{
    font-family:"Norican",cursive;font-size:36px;letter-spacing:0;
    margin-left:6px;display:inline-block;
  }
  .hours__time{
    margin:4px 0 0;font-family:"Yanone Kaffeesatz",sans-serif;font-weight:400;
    font-size:40px;line-height:50px;color:var(--white);
  }
</style>
</head>
<body>
<main class="card" aria-label="Harlow Commons opening hours">
  <div class="bar bar--corner"></div>
  <div class="bar bar--top"></div>
  <div class="bar bar--side"></div>
  <div class="bar band"></div>
  <div class="bar column"></div>

  <h1 class="name-row">HARLOW</h1>
  <p class="name-column" aria-label="Commons">
    <span>C</span><span>O</span><span>M</span><span>M</span><span>O</span><span>N</span><span>S</span>
  </p>

  <p class="address"><span class="address__label">ADDRESS</span>54-16 Benning Street Forest Hills, NY 11382</p>
  <p class="phone"><span class="phone__label">PHONE</span>718.555.0143</p>

  <section class="hours hours--lunch">
    <h2 class="hours__title">LUNCH<span class="hours__served">served</span></h2>
    <p class="hours__time">Monday to Friday 10 a.m. - 3 p.m.</p>
  </section>
  <section class="hours hours--dinner">
    <h2 class="hours__title">DINNER<span class="hours__served">served</span></h2>
    <p class="hours__time">Sunday - Monday 3 p.m. - 11 p.m.</p>
  </section>
  <section class="hours hours--brunch">
    <h2 class="hours__title">BRUNCH<span class="hours__served">served</span></h2>
    <p class="hours__time">Saturday &amp; Sunday</p>
  </section>
  <section class="hours hours--late">
    <h2 class="hours__title">LATE NIGHT<br><span class="hours__served" style="margin-left:0">Bar Menu served</span></h2>
    <p class="hours__time">Thursday, Friday &amp; Saturday<br>from 11 p.m. - 1 a.m.</p>
  </section>
</main>
</body>
</html>
```